Plumwave business card

We need a modern business card - With our 4 colors - See web: www.plumwave.dk

I have attached logo and som old business Cards we have - Lets Make the new ones shine...:-) -

Industry/Entity Type

Business

Requirements
Must have
• the logo with plumwave only,

```html
<!DOCTYPE html>
<html lang="da">
<head>
<meta charset="utf-8">
<title>Plumwave business card</title>
<link href="https://fonts.googleapis.com/css2?family=Raleway:wght@400;500&display=swap" rel="stylesheet">
<style>
  :root {
    --backdrop: #e9e6e1;
    --card-dark: #3b3b3d;
    --card-dark-edge: #2e2e30;
    --card-light: #f7f7f5;
    --lime: #a9cf38;
    --magenta: #d2168f;
    --purple: #8a2f8c;
    --orange: #ef9f25;
    --ink-light: #f1f1f1;
    --ink-grey: #6c6c6c;
  }
  * { margin: 0; padding: 0; box-sizing: border-box; }
  html, body { width: 1200px; height: 780px; overflow: hidden; }
  body {
    background: var(--backdrop);
    font-family: "Raleway", sans-serif;
    display: flex;
    align-items: center;
    justify-content: center;
    gap: 60px;
  }
  .card {
    width: 520px;
    height: 320px;
    border-radius: 4px;
    box-shadow: 0 10px 26px rgba(0,0,0,.18);
    overflow: hidden;
    position: relative;
  }

  /* Front: split card */
  .card--front { display: flex; }
  .front__brand {
    width: 42%;
    background: var(--card-light);
    display: flex;
    flex-direction: column;
    align-items: center;
    justify-content: center;
  }
  .brand-mark {
    display: flex;
    align-items: center;
    gap: 10px;
    color: var(--ink-grey);
    font-size: 22px;
    font-weight: 400;
    letter-spacing: 4px;
  }
  .brand-mark__dot {
    width: 14px; height: 14px; border-radius: 50%;
    background: var(--lime);
  }
  .front__rule {
    width: 150px; height: 2px; background: var(--lime);
    margin: 14px 0 10px;
  }
  .front__tagline { font-size: 11px; color: var(--ink-grey); }

  .front__contact {
    flex: 1;
    background: var(--card-dark);
    color: var(--ink-light);
    padding: 44px 34px;
    font-size: 13px;
    line-height: 1.45;
  }
  .contact__name { color: var(--lime); font-size: 21px; font-weight: 500; line-height: 1.1; }
  .contact__title { font-size: 13px; margin-bottom: 22px; }
  .contact__address { margin-bottom: 18px; }
  .contact__lines { display: flex; gap: 10px; align-items: center; margin-bottom: 6px; }
  .contact__icons { display: flex; flex-direction: column; gap: 3px; }
  .contact__icon {
    width: 16px; height: 16px; background: var(--lime);
    display: flex; align-items: center; justify-content: center;
  }
  .contact__web { color: var(--lime); font-weight: 500; }

  /* Back: dark card */
  .card--back {
    background: radial-gradient(circle at 60% 40%, #434345, var(--card-dark) 60%, var(--card-dark-edge));
    color: var(--ink-light);
    display: flex;
    flex-direction: column;
    align-items: center;
    justify-content: center;
  }
  .card--back .brand-mark { color: var(--ink-light); font-size: 28px; letter-spacing: 6px; }
  .back__service { font-size: 18px; letter-spacing: 1px; margin: 22px 0 14px; }
  .back__areas { font-size: 12.5px; letter-spacing: .5px; color: var(--ink-light); }
  .area--study { color: var(--purple); }
  .area--life { color: var(--magenta); }
  .area--urban { color: var(--lime); }
  .area--social { color: var(--orange); }
</style>
</head>
<body>

  <section class="card card--front" aria-label="Visitkort forside">
    <div class="front__brand">
      <div class="brand-mark"><span class="brand-mark__dot"></span>plumwave</div>
      <div class="front__rule"></div>
      <p class="front__tagline">Medier til unge</p>
    </div>
    <div class="front__contact">
      <p class="contact__name">Malte Hvidberg</p>
      <p class="contact__title">Salgsdirektør</p>
      <p class="contact__address">Lindelundsvej 14<br>2500 Valby</p>
      <div class="contact__lines">
        <div class="contact__icons">
          <span class="contact__icon"><svg width="10" height="10" viewBox="0 0 10 10"><rect x="1" y="1" width="8" height="8" rx="1" fill="none" stroke="#3b3b3d" stroke-width="1.3"/><line x1="3" y1="4" x2="7" y2="4" stroke="#3b3b3d"/></svg></span>
          <span class="contact__icon"><svg width="10" height="10" viewBox="0 0 10 10"><rect x="3" y="1" width="4" height="8" rx="1" fill="none" stroke="#3b3b3d" stroke-width="1.2"/></svg></span>
          <span class="contact__icon"><svg width="10" height="10" viewBox="0 0 10 10"><rect x="1" y="2" width="8" height="6" fill="none" stroke="#3b3b3d" stroke-width="1.2"/><polyline points="1,2 5,6 9,2" fill="none" stroke="#3b3b3d" stroke-width="1.2"/></svg></span>
        </div>
        <div>
          <p>+45 60 12 34 78</p>
          <p>+45 31 47 90 62</p>
          <p>mh@plumwave.dk</p>
        </div>
      </div>
      <p class="contact__web">www.plumwave.dk</p>
    </div>
  </section>

  <section class="card card--back" aria-label="Visitkort bagside">
    <div class="brand-mark"><span class="brand-mark__dot"></span>plumwave</div>
    <p class="back__service">SERVICE</p>
    <p class="back__areas">
      <span class="area--study">STUDIELIV</span> | <span class="area--life">LIVSTIL</span> | <span class="area--urban">URBAN &amp; EVENT</span> | <span class="area--social">SOCIAL</span>
    </p>
  </section>

</body>
</html>
```